Stationery Set for new venture capital firm

We need a new set of stationery including letterhead, business cards, envelopes, with compliment slips for our new startup venture capital firm known as Halvora.
We make alternative investments globally and hope to have a worldwide network of offices later.

The stationery should be elegant and not too fussy with the use of too many colors.

Venture Capital

```html
<!DOCTYPE html>
<html lang="en">
<head>
<meta charset="utf-8">
<title>Halvora Stationery Set</title>
<link rel="stylesheet" href="https://fonts.googleapis.com/css2?family=Open+Sans:wght@300;400;600;700&display=swap">
<style>
  :root {
    --brand-blue: #4aa3d6;
    --paper: #ffffff;
    --backdrop: #ececec;
    --ink: #6f6f6f;
    --ink-soft: #9a9a9a;
    --rule: #cfcfcf;
  }
  * { box-sizing: border-box; margin: 0; padding: 0; }
  html, body { width: 1200px; height: 1000px; overflow: hidden; }
  body {
    background: var(--backdrop);
    font-family: "Open Sans", sans-serif;
    color: var(--ink);
    position: relative;
  }
  .sheet {
    position: absolute;
    background: var(--paper);
    box-shadow: 0 2px 6px rgba(0,0,0,0.12);
    overflow: hidden;
  }
  .wordmark {
    display: flex;
    align-items: center;
    gap: 6px;
    font-weight: 700;
    color: var(--ink);
  }
  .wordmark-dot {
    border-radius: 50%;
    background: var(--brand-blue);
    flex: none;
  }

  /* Business card front */
  .card-front {
    left: 90px; top: 110px; width: 260px; height: 150px;
    background: var(--brand-blue);
  }
  .card-front .art { position: absolute; inset: 0; background: var(--brand-blue); }

  /* Business card back */
  .card-back { left: 380px; top: 110px; width: 260px; height: 150px; }
  .card-back .wordmark { position: absolute; left: 18px; top: 18px; font-size: 13px; }
  .card-back .wordmark-dot { width: 12px; height: 12px; }
  .card-back .holder { position: absolute; left: 18px; top: 52px; }
  .card-back .holder-name { font-size: 12px; color: var(--brand-blue); font-weight: 400; }
  .card-back .holder-role { font-size: 7px; color: var(--ink-soft); font-style: italic; }
  .card-back .corner-disc {
    position: absolute; left: 120px; top: 70px; width: 220px; height: 220px;
    border-radius: 50%; background: var(--brand-blue);
  }
  .card-back .contact {
    position: absolute; left: 168px; top: 88px; font-size: 5.5px; line-height: 1.5; color: #fff;
  }

  /* Compliment slip */
  .slip { left: 90px; top: 300px; width: 550px; height: 260px; background: var(--brand-blue); }
  .slip .art { position: absolute; inset: 0; background: var(--brand-blue); }

  /* Envelope */
  .envelope { left: 90px; top: 600px; width: 550px; height: 280px; }
  .envelope .flap-band { position: absolute; left: 0; right: 0; top: 0; height: 38px; background: var(--paper); }
  .envelope .body-band { position: absolute; left: 0; right: 0; top: 38px; bottom: 0; background: var(--brand-blue); }
  .envelope .sender { position: absolute; right: 24px; bottom: 22px; width: 120px; }
  .envelope .wordmark { color: #fff; font-size: 14px; margin-bottom: 8px; }
  .envelope .wordmark-dot { width: 12px; height: 12px; background: #fff; }
  .envelope .sender-lines { font-size: 6px; line-height: 1.5; color: #fff; }

  /* Letterhead */
  .letterhead { left: 680px; top: 110px; width: 440px; height: 780px; }
  .letterhead .wordmark {
    position: absolute; left: 0; right: 0; top: 46px; justify-content: center; font-size: 22px;
  }
  .letterhead .wordmark-dot { width: 18px; height: 18px; }
  .meta { position: absolute; left: 30px; top: 132px; width: 80px; }
  .meta dt { font-size: 7px; font-weight: 700; color: var(--brand-blue); text-transform: uppercase; line-height: 1.2; }
  .meta dd { font-size: 7px; color: var(--ink-soft); margin-bottom: 5px; line-height: 1.2; }
  .letter {
    position: absolute; left: 118px; top: 132px; right: 30px;
    border-left: 1px solid var(--rule); padding-left: 14px;
  }
  .letter-heading { font-size: 11px; font-weight: 300; color: var(--ink-soft); margin-bottom: 12px; }
  .letter-heading strong { font-weight: 600; color: var(--brand-blue); }
  .letter p { font-size: 6.5px; line-height: 1.65; color: var(--ink-soft); margin-bottom: 12px; }
  .sign-off { position: absolute; left: 300px; top: 520px; text-align: center; width: 100px; }
  .sign-off .role { font-size: 7px; color: var(--ink-soft); margin-bottom: 6px; }
  .signature { width: 100px; height: 30px; background: linear-gradient(90deg, #e6e6e6, #d6d6d6); border-radius: 4px; }
  .letterhead .corner-disc {
    position: absolute; left: 190px; top: 610px; width: 360px; height: 360px;
    border-radius: 50%; background: var(--brand-blue);
  }
  .letterhead .contact {
    position: absolute; left: 300px; top: 628px; font-size: 6px; line-height: 1.55; color: #fff;
  }
  .letterhead .contact strong { font-weight: 700; }
</style>
</head>
<body>

<section class="sheet card-front" aria-label="Business card front">
  <div class="art" role="img" aria-label="Brand mascot eyes in white on blue"></div>
</section>

<section class="sheet card-back" aria-label="Business card back">
  <div class="wordmark"><span class="wordmark-dot"></span>Halvora</div>
  <div class="holder">
    <div class="holder-name">Marta Lindqvist</div>
    <div class="holder-role">Chief Executive Officer</div>
  </div>
  <div class="corner-disc"></div>
  <div class="contact">
    Halvora Venture Capital<br>
    18 Harbour Lane, Level 4<br>
    Oslo 0150, Norway<br>
    +47 2200 4410<br>
    hello@halvora-vc.com
  </div>
</section>

<section class="sheet slip" aria-label="Compliment slip">
  <div class="art" role="img" aria-label="Large white brand mascot with tentacles on blue"></div>
</section>

<section class="sheet envelope" aria-label="Envelope">
  <div class="flap-band"></div>
  <div class="body-band"></div>
  <div class="sender">
    <div class="wordmark"><span class="wordmark-dot"></span>Halvora</div>
    <div class="sender-lines">
      Halvora Venture Capital<br>
      18 Harbour Lane, Level 4<br>
      Oslo 0150, Norway<br>
      +47 2200 4410<br>
      hello@halvora-vc.com
    </div>
  </div>
</section>

<section class="sheet letterhead" aria-label="Letterhead">
  <div class="wordmark"><span class="wordmark-dot"></span>Halvora</div>

  <dl class="meta">
    <dt>Subject</dt><dd>Lorem ipsum</dd>
    <dt>Date</dt><dd>01.05.2014</dd>
    <dt>Adressed to</dt><dd>Jane Doe</dd>
  </dl>

  <div class="letter">
    <h1 class="letter-heading"><strong>Nulla sodales:</strong> Lorem ipsum dolor sit ametconsectetur</h1>
    <p>Dear Client,</p>
    <p>Lorem ipsum dolor sit amet, consectetur adipiscing elit. Nulla sodales nisi vitae lorem ipsum dolor sit amet, consectetur adipiscing elit. Suspendisse feugiat eros nisi, a facilisis risus eleifend sed. Aliquam rhoncus enim at justo fermentum, eu egestas sit amet. Integer sit amet laoreet nibh, nec convallis lorem. Vivamus a sapien blandit, tincidunt justo id, euismod massa. Phasellus at sapien eget nunc tristique iaculis ut vel tortor. Nam pharetra velit molestie justo placerat scelerisque.</p>
    <p>Ut vitae interdum diam, in euismod ante. Pellentesque volutpat risus sit amet sodales hendrerit, in luctus vulputate dolor eget cursus. Nulla tincidunt molestie libero vel pretium. Donec condimentum nulla sit amet nisi semper imperdiet. Duis congue erat nec diam iaculis. Etiam at ornare metus. Curabitur tristique venenatis velit, ut volutpat nisi mattis eget. Aliquam erat volutpat. Mauris nisi leo, egestas at dolor a, ultricies aliquet est. Nunc faucibus scelerisque nunc, vel tempor ligula malesuada at. Fusce in quam sapien.</p>
    <p>Best regards,</p>
  </div>

  <div class="sign-off">
    <div class="role">Director</div>
    <div class="signature" role="img" aria-label="Handwritten signature of Marta Lindqvist"></div>
  </div>

  <div class="corner-disc"></div>
  <div class="contact">
    <strong>Halvora Venture Capital</strong><br>
    18 Harbour Lane, Level 4<br>
    Oslo 0150, Norway<br>
    +47 2200 4410<br>
    hello@halvora-vc.com
  </div>
</section>

</body>
</html>
```